Rebrand of 3 bottle labels for nail polish brand

The task is to make a rebranding of our current gel nail polish bottle design. We have become one of the leading european nail polish brand, so we want to improve the quality of the label design to a more scandinavian and minimalistic bottle design, which stille has to be recognisable and unique.

We have attached a more detailed description of the rebranding instructions for our gel polish bottles called "bottle task".
Updates

The Labels should not be just Black and White as stated. But should be mainly Black and White and then some of our color as explained in the uploaded file.

Target Market(s)

Girls and women age 18-55 Northern Europe

Industry/Entity Type

Cosmetic/ Nail Gel Polish

Colors

Designer to choose only greyscale colors for use in the design.

Requirements
Must have
• See attched design instruction
Nice to have
• Moderne, Minimalist, Recognizable and Unique look
Should not have
• Too many elements, too busy design

```html
<!DOCTYPE html>
<html lang="en">
<head>
<meta charset="utf-8">
<title>Velmora gel polish labels</title>
<link rel="stylesheet" href="https://fonts.googleapis.com/css2?family=Quicksand:wght@300;400;500;600&display=swap">
<style>
  :root {
    --page: #f1e4e2;
    --label: #231f20;
    --white: #ffffff;
    --muted: #bdb6b4;
    --blush: #d4bcb3;
    --lemon: #ece684;
    --ink: #231f20;
    --bottle: #141213;
    --bottle-light: #2e2a2b;
  }
  * { margin: 0; padding: 0; box-sizing: border-box; }
  html, body { width: 1200px; height: 2901px; overflow: hidden; }
  body {
    background: var(--page);
    font-family: "Quicksand", sans-serif;
    position: relative;
    color: var(--white);
  }

  /* ---------- bottles ---------- */
  .bottle { position: absolute; }
  .bottle .cap {
    position: absolute; top: 0;
    border-radius: 46px 46px 8px 8px;
    background: linear-gradient(90deg, #0e0d0d 0%, #2c2929 40%, #1a1818 70%, #0b0a0a 100%);
  }
  .bottle .body {
    position: absolute; left: 0; right: 0; bottom: 0;
    border-radius: 80px 80px 40px 40px;
    background: linear-gradient(90deg, var(--bottle) 0%, var(--bottle-light) 40%, var(--bottle) 100%);
    overflow: hidden;
  }
  .bottle .band {
    position: absolute; left: 0; right: 0; height: 42px;
    color: var(--ink); font-size: 17px; font-weight: 500; letter-spacing: 2px;
    display: flex; align-items: center;
  }
  .bottle.blush .band { background: linear-gradient(90deg, #c7aea5, #dcc6be 45%, #c7aea5); }
  .bottle.lemon .band { background: linear-gradient(90deg, #dcd56c, #f1ec92 45%, #d8d064); }
  .bottle .b-brand { position: absolute; font-size: 42px; font-weight: 400; line-height: 1; }
  .bottle .b-brand.vertical { writing-mode: vertical-rl; transform: rotate(180deg); font-size: 44px; }
  .bottle .b-name { position: absolute; font-size: 21px; font-weight: 500; letter-spacing: 1px; white-space: nowrap; }
  .bottle .b-tech { display: block; font-size: 14px; font-weight: 400; color: var(--muted); letter-spacing: 0.3px; margin-top: 2px; }
  .bottle .b-num { position: absolute; font-size: 24px; }
  .bottle .b-claim { position: absolute; font-size: 15px; color: var(--muted); }
  .bottle .b-leaf { position: absolute; width: 22px; height: 28px; border-radius: 50% 0 50% 0; }
  .bottle.blush .b-leaf, .bottle.blush .b-chip { background: var(--blush); }
  .bottle.lemon .b-leaf, .bottle.lemon .b-chip { background: var(--lemon); }
  .bottle .b-chip { position: absolute; left: 0; width: 24px; height: 44px; border-radius: 0 10px 10px 0; }

  .option-tag {
    position: absolute; font-weight: 500; font-size: 21px; color: var(--ink);
  }

  /* ---------- flat labels ---------- */
  .label {
    position: absolute; left: 160px; width: 873px; height: 232px;
    background: var(--label); overflow: hidden;
  }
  .label.short { height: 204px; }
  .label .strip {
    position: absolute; left: 0; right: 0; bottom: 0; height: 44px;
    display: flex; align-items: center;
    font-size: 12.5px; font-weight: 500; color: var(--ink);
  }
  .label.short .strip { height: 40px; }
  .label.blush .strip { background: var(--blush); }
  .label.lemon .strip { background: var(--lemon); }
  .strip .shade { position: absolute; left: 171px; letter-spacing: 1.6px; font-size: 13px; }
  .strip .volume { position: absolute; left: 342px; }
  .label.short .strip .volume { left: 360px; }
  .strip .maker { position: absolute; left: 455px; font-size: 11.5px; }

  .brand { position: absolute; font-weight: 400; font-size: 38px; color: var(--white); line-height: 1; }
  .brand.horizontal { left: 133px; top: 28px; }
  .brand.vertical {
    writing-mode: vertical-rl; transform: rotate(180deg);
    left: 86px; top: 22px; font-size: 40px;
  }
  .label.short .brand.vertical { top: 20px; font-size: 34px; }

  .product { position: absolute; left: 171px; top: 78px; }
  .product .name { font-size: 17px; font-weight: 500; letter-spacing: 1px; }
  .product .tech { font-size: 11px; color: var(--muted); letter-spacing: 0.4px; margin-top: 1px; }
  .product .number { font-size: 20px; margin-top: 14px; }
  .product .claim { font-size: 11.5px; color: var(--muted); margin-top: 12px; }
  .label.short .product { top: 70px; }
  .label.short .product .number { margin-top: 8px; }
  .label.short .product .claim { margin-top: 6px; }

  .leaf-mark { position: absolute; width: 24px; height: 28px; border-radius: 50% 0 50% 0; }
  .label.blush .leaf-mark, .label.blush .corner-chip { background: var(--blush); }
  .label.lemon .leaf-mark, .label.lemon .corner-chip { background: var(--lemon); }
  .corner-chip { position: absolute; left: 32px; top: 0; width: 42px; height: 28px; border-radius: 0 0 12px 12px; }

  .info {
    position: absolute; left: 456px; top: 10px; width: 408px;
    font-size: 9px; line-height: 10.6px; color: var(--white); letter-spacing: -0.2px;
  }
  .info p { margin-bottom: 0.5px; }
  .info b { font-weight: 600; }
  .made-in { position: absolute; left: 456px; font-size: 9.6px; font-weight: 500; }
  .symbols { position: absolute; left: 670px; display: flex; gap: 12px; }
  .symbols svg { width: 24px; height: 24px; }
</style>
</head>
<body>

  <!-- Bottle: base coat, option 1 -->
  <div class="bottle blush" style="left:212px;top:95px;width:297px;height:740px;">
    <div class="cap" style="left:63px;width:150px;height:370px;"></div>
    <div class="body" style="height:385px;">
      <div class="b-brand" style="left:48px;top:85px;">Velmora</div>
      <div class="b-name" style="left:56px;top:140px;">BASE COAT<span class="b-tech">SOAK OFF UV/LED</span></div>
      <div class="b-num" style="left:56px;top:195px;">01</div>
      <div class="b-leaf" style="left:12px;top:232px;"></div>
      <div class="b-claim" style="left:56px;top:238px;">Vegan Formula</div>
      <div class="band" style="top:270px;padding-left:56px;">FLEXIBLE</div>
    </div>
  </div>

  <!-- Bottle: base coat, option 2 -->
  <div class="bottle lemon" style="left:683px;top:88px;width:299px;height:747px;">
    <div class="cap" style="left:65px;width:157px;height:380px;"></div>
    <div class="body" style="height:375px;">
      <div class="b-brand vertical" style="left:27px;top:70px;">Velmora</div>
      <div class="b-name" style="left:97px;top:135px;">BASE COAT<span class="b-tech">SOAK OFF UV/LED</span></div>
      <div class="b-num" style="left:97px;top:195px;">01</div>
      <div class="b-claim" style="left:97px;top:248px;">Vegan Formula</div>
      <div class="b-leaf" style="left:240px;top:232px;"></div>
      <div class="band" style="top:270px;padding-left:97px;">COLOR NAME</div>
    </div>
  </div>

  <!-- Bottle: color coat, option 1 -->
  <div class="bottle blush" style="left:154px;top:1548px;width:302px;height:775px;">
    <div class="cap" style="left:63px;width:180px;height:370px;"></div>
    <div class="body" style="height:423px;">
      <div class="b-chip" style="top:50px;"></div>
      <div class="b-brand" style="left:48px;top:90px;">Velmora</div>
      <div class="b-name" style="left:66px;top:140px;">COLOR COAT<span class="b-tech">SOAK OFF UV/LED</span></div>
      <div class="b-num" style="left:66px;top:200px;">01</div>
      <div class="b-claim" style="left:66px;top:245px;">Vegan Formula</div>
      <div class="b-leaf" style="left:250px;top:232px;"></div>
      <div class="band" style="top:275px;padding-left:66px;">COLOR NAME</div>
    </div>
  </div>

  <!-- Bottle: color coat, option 2 -->
  <div class="bottle lemon" style="left:651px;top:1570px;width:297px;height:752px;">
    <div class="cap" style="left:57px;width:175px;height:360px;"></div>
    <div class="body" style="height:397px;">
      <div class="b-chip" style="top:15px;"></div>
      <div class="b-brand vertical" style="left:58px;top:75px;">Velmora</div>
      <div class="b-name" style="left:139px;top:125px;">COLOR COAT<span class="b-tech">SOAK OFF UV/LED</span></div>
      <div class="b-num" style="left:139px;top:185px;">01</div>
      <div class="b-claim" style="left:139px;top:240px;">Vegan Formula</div>
      <div class="b-leaf" style="left:250px;top:222px;"></div>
      <div class="band" style="top:268px;padding-left:139px;">COLOR NAME</div>
    </div>
  </div>

  <div class="option-tag" style="left:1077px;top:1023px;">OP1</div>
  <div class="option-tag" style="left:1073px;top:1296px;">OP2</div>

  <!-- Base coat label, option 1 -->
  <section class="label blush" style="top:907px;">
    <div class="brand horizontal">Velmora</div>
    <div class="product">
      <div class="name">BASE COAT</div>
      <div class="tech">SOAK OFF UV/LED</div>
      <div class="number">01</div>
      <div class="claim">Vegan Formula</div>
    </div>
    <div class="leaf-mark" style="left:124px;top:155px;"></div>
    <div class="info">
      <p><b>DIRECTIONS FOR USE (ENG):</b> Velmora Base Coat must be applied in thin layers and cured in one of our Velmora Lamps.</p>
      <p><b>ANVENDELSE (DK):</b> Velmora Base Coat skal påføres i tynde lag og hærdes i en af vores Velmora Lamper.</p>
      <p><b>CAUTION (ENG):</b> Keep out of reach of children. Discontinue use if irritation occurs. Avoid direct sunlight or extreme exposure to LED or UV light.</p>
      <p><b>ADVARSEL (DK):</b> Opbevar utilgængeligt for børn. Stop din behandling, hvis produktet forudsager irritation. Undgå direkte sollys eller udsættelse for LED eller UV.</p>
      <p><b>INGREDIENTS:</b> Acrylates Copolymer, Acrylated Aliphatic Urethane, Cellulose Acetate Butanoate, Dimethicone, Ceresine, wax , Pigment Red, Carbon Black, Titanium dioxide, CI 77891</p>
    </div>
    <div class="made-in" style="top:162px;">Made in Europe</div>
    <div class="symbols" style="top:156px;">
      <svg viewBox="0 0 24 24"><path d="M12 1 23 12 12 23 1 12Z" fill="#fff"/><path d="M12 4.5 19.5 12 12 19.5 4.5 12Z" fill="var(--label)"/><rect x="11" y="7.5" width="2" height="6" fill="#fff"/><rect x="11" y="15" width="2" height="2" fill="#fff"/></svg>
      <svg viewBox="0 0 24 24" fill="none" stroke="#fff" stroke-width="1.4"><path d="M4 7h16l-1.5 13h-13Z"/><path d="M5 7l2-3h10l2 3"/><text x="12" y="17" font-size="6" fill="#fff" stroke="none" text-anchor="middle" font-family="Quicksand, sans-serif">24M</text></svg>
      <svg viewBox="0 0 24 24" fill="none" stroke="#fff" stroke-width="1.4"><path d="M8 5l4-2 3 5M19 12l1 5h-6M6 19l-3-4 3-4"/><path d="M13 6l2 2-3 0M15 17l-2 2 0-3M5 13l1-2 2 2"/></svg>
      <svg viewBox="0 0 24 24" fill="none" stroke="#fff" stroke-width="1.4"><path d="M6 20v-6l3-3 2 2V5a1.5 1.5 0 0 1 3 0v7h3a2 2 0 0 1 2 2v6"/><rect x="14" y="2" width="5" height="6" rx="1"/></svg>
      <svg viewBox="0 0 24 24" fill="none" stroke="#fff" stroke-width="1.4"><circle cx="12" cy="8" r="4"/><circle cx="8" cy="13" r="4"/><circle cx="16" cy="13" r="4"/><text x="12" y="23.5" font-size="4" fill="#fff" stroke="none" text-anchor="middle" font-family="Quicksand, sans-serif">VEGAN</text></svg>
    </div>
    <div class="strip">
      <span class="shade">COLOR NAME</span>
      <span class="volume">15ml e 0.5oz</span>
      <span class="maker">Nordlys Studio A/S – Havnevej 12, 2450 Copenhagen, Denmark</span>
    </div>
  </section>

  <!-- Base coat label, option 2 -->
  <section class="label lemon" style="top:1193px;">
    <div class="brand vertical">Velmora</div>
    <div class="product">
      <div class="name">BASE COAT</div>
      <div class="tech">SOAK OFF UV/LED</div>
      <div class="number">01</div>
      <div class="claim">Vegan Formula</div>
    </div>
    <div class="leaf-mark" style="left:282px;top:152px;"></div>
    <div class="info">
      <p><b>DIRECTIONS FOR USE (ENG):</b> Velmora Base Coat must be applied in thin layers and cured in one of our Velmora Lamps.</p>
      <p><b>ANVENDELSE (DK):</b> Velmora Base Coat skal påføres i tynde lag og hærdes i en af vores Velmora Lamper.</p>
      <p><b>CAUTION (ENG):</b> Keep out of reach of children. Discontinue use if irritation occurs. Avoid direct sunlight or extreme exposure to LED or UV light.</p>
      <p><b>ADVARSEL (DK):</b> Opbevar utilgængeligt for børn. Stop din behandling, hvis produktet forudsager irritation. Undgå direkte sollys eller udsættelse for LED eller UV.</p>
      <p><b>INGREDIENTS:</b> Acrylates Copolymer, Acrylated Aliphatic Urethane, Cellulose Acetate Butanoate, Dimethicone, Ceresine, wax , Pigment Red, Carbon Black, Titanium dioxide, CI 77891</p>
    </div>
    <div class="made-in" style="top:162px;">Made in Europe</div>
    <div class="symbols" style="top:156px;">
      <svg viewBox="0 0 24 24"><path d="M12 1 23 12 12 23 1 12Z" fill="#fff"/><path d="M12 4.5 19.5 12 12 19.5 4.5 12Z" fill="var(--label)"/><rect x="11" y="7.5" width="2" height="6" fill="#fff"/><rect x="11" y="15" width="2" height="2" fill="#fff"/></svg>
      <svg viewBox="0 0 24 24" fill="none" stroke="#fff" stroke-width="1.4"><path d="M4 7h16l-1.5 13h-13Z"/><path d="M5 7l2-3h10l2 3"/><text x="12" y="17" font-size="6" fill="#fff" stroke="none" text-anchor="middle" font-family="Quicksand, sans-serif">24M</text></svg>
      <svg viewBox="0 0 24 24" fill="none" stroke="#fff" stroke-width="1.4"><path d="M8 5l4-2 3 5M19 12l1 5h-6M6 19l-3-4 3-4"/><path d="M13 6l2 2-3 0M15 17l-2 2 0-3M5 13l1-2 2 2"/></svg>
      <svg viewBox="0 0 24 24" fill="none" stroke="#fff" stroke-width="1.4"><path d="M6 20v-6l3-3 2 2V5a1.5 1.5 0 0 1 3 0v7h3a2 2 0 0 1 2 2v6"/><rect x="14" y="2" width="5" height="6" rx="1"/></svg>
      <svg viewBox="0 0 24 24" fill="none" stroke="#fff" stroke-width="1.4"><circle cx="12" cy="8" r="4"/><circle cx="8" cy="13" r="4"/><circle cx="16" cy="13" r="4"/><text x="12" y="23.5" font-size="4" fill="#fff" stroke="none" text-anchor="middle" font-family="Quicksand, sans-serif">VEGAN</text></svg>
    </div>
    <div class="strip">
      <span class="shade">COLOR NAME</span>
      <span class="volume">15ml e 0.5oz</span>
      <span class="maker">Nordlys Studio A/S – Havnevej 12, 2450 Copenhagen, Denmark</span>
    </div>
  </section>

  <!-- Color coat label, option 1 -->
  <section class="label blush short" style="top:2399px;">
    <div class="corner-chip"></div>
    <div class="brand horizontal" style="top:22px;">Velmora</div>
    <div class="product">
      <div class="name">COLOR COAT</div>
      <div class="tech">SOAK OFF UV/LED</div>
      <div class="number">01</div>
      <div class="claim">Vegan Formula</div>
    </div>
    <div class="leaf-mark" style="left:290px;top:128px;"></div>
    <div class="info" style="top:8px;">
      <p><b>DIRECTIONS FOR USE (ENG):</b> Velmora Base Coat must be applied in thin layers and cured in one of our Velmora Lamps.</p>
      <p><b>ANVENDELSE (DK):</b> Velmora Base Coat skal påføres i tynde lag og hærdes i en af vores Velmora Lamper.</p>
      <p><b>CAUTION (ENG):</b> Keep out of reach of children. Discontinue use if irritation occurs. Avoid direct sunlight or extreme exposure to LED or UV light.</p>
      <p><b>ADVARSEL (DK):</b> Opbevar utilgængeligt for børn. Stop din behandling, hvis produktet forudsager irritation. Undgå direkte sollys eller udsættelse for LED eller UV.</p>
      <p><b>INGREDIENTS:</b> Acrylates Copolymer, Acrylated Aliphatic Urethane, Cellulose Acetate Butanoate, Dimethicone, Ceresine, wax , Pigment Red, Carbon Black, Titanium dioxide, CI 77891</p>
    </div>
    <div class="made-in" style="top:140px;">Made in Europe</div>
    <div class="symbols" style="top:134px;">
      <svg viewBox="0 0 24 24"><path d="M12 1 23 12 12 23 1 12Z" fill="#fff"/><path d="M12 4.5 19.5 12 12 19.5 4.5 12Z" fill="var(--label)"/><rect x="11" y="7.5" width="2" height="6" fill="#fff"/><rect x="11" y="15" width="2" height="2" fill="#fff"/></svg>
      <svg viewBox="0 0 24 24" fill="none" stroke="#fff" stroke-width="1.4"><path d="M4 7h16l-1.5 13h-13Z"/><path d="M5 7l2-3h10l2 3"/><text x="12" y="17" font-size="6" fill="#fff" stroke="none" text-anchor="middle" font-family="Quicksand, sans-serif">24M</text></svg>
      <svg viewBox="0 0 24 24" fill="none" stroke="#fff" stroke-width="1.4"><path d="M8 5l4-2 3 5M19 12l1 5h-6M6 19l-3-4 3-4"/><path d="M13 6l2 2-3 0M15 17l-2 2 0-3M5 13l1-2 2 2"/></svg>
      <svg viewBox="0 0 24 24" fill="none" stroke="#fff" stroke-width="1.4"><path d="M6 20v-6l3-3 2 2V5a1.5 1.5 0 0 1 3 0v7h3a2 2 0 0 1 2 2v6"/><rect x="14" y="2" width="5" height="6" rx="1"/></svg>
      <svg viewBox="0 0 24 24" fill="none" stroke="#fff" stroke-width="1.4"><circle cx="12" cy="8" r="4"/><circle cx="8" cy="13" r="4"/><circle cx="16" cy="13" r="4"/><text x="12" y="23.5" font-size="4" fill="#fff" stroke="none" text-anchor="middle" font-family="Quicksand, sans-serif">VEGAN</text></svg>
    </div>
    <div class="strip">
      <span class="shade">COLOR NAME</span>
      <span class="volume">15ml e 0.5oz</span>
      <span class="maker">Nordlys Studio A/S – Havnevej 12, 2450 Copenhagen, Denmark</span>
    </div>
  </section>

  <!-- Color coat label, option 2 -->
  <section class="label lemon short" style="top:2643px;">
    <div class="corner-chip"></div>
    <div class="brand vertical">Velmora</div>
    <div class="product">
      <div class="name">COLOR COAT</div>
      <div class="tech">SOAK OFF UV/LED</div>
      <div class="number">01</div>
      <div class="claim">Vegan Formula</div>
    </div>
    <div class="leaf-mark" style="left:282px;top:128px;"></div>
    <div class="info" style="top:8px;">
      <p><b>DIRECTIONS FOR USE (ENG):</b> Velmora Color Coat must be applied in thin layers and cured in one of our Velmora Lamps.</p>
      <p><b>ANVENDELSE (DK):</b> Velmora Farver skal påføres i tynde lag og hærdes i en af vores Velmora Lamper.</p>
      <p><b>CAUTION (ENG):</b> Keep out of reach of children. Discontinue use if irritation occurs. Avoid direct sunlight or extreme exposure to LED or UV Light.</p>
      <p><b>ADVARSEL (DK):</b> Opbevar utilgængeligt for børn. Stop din behandling, hvis produktet forudsager irritation. Undgå direkte sollys eller udsættelse for LED eller UV.</p>
      <p><b>INGREDIENTS:</b> Acrylates Copolymer, Acrylated Aliphatic Urethane, Cellulose Acetate Butanoate, Dimethicone, Ceresine, wax , Pigment Red, Carbon Black, Titanium dioxide, CI 77891</p>
    </div>
    <div class="made-in" style="top:140px;">Made in Germany</div>
    <div class="symbols" style="top:134px;">
      <svg viewBox="0 0 24 24"><path d="M12 1 23 12 12 23 1 12Z" fill="#fff"/><path d="M12 4.5 19.5 12 12 19.5 4.5 12Z" fill="var(--label)"/><rect x="11" y="7.5" width="2" height="6" fill="#fff"/><rect x="11" y="15" width="2" height="2" fill="#fff"/></svg>
      <svg viewBox="0 0 24 24" fill="none" stroke="#fff" stroke-width="1.4"><path d="M4 7h16l-1.5 13h-13Z"/><path d="M5 7l2-3h10l2 3"/><text x="12" y="17" font-size="6" fill="#fff" stroke="none" text-anchor="middle" font-family="Quicksand, sans-serif">24M</text></svg>
      <svg viewBox="0 0 24 24" fill="none" stroke="#fff" stroke-width="1.4"><path d="M8 5l4-2 3 5M19 12l1 5h-6M6 19l-3-4 3-4"/><path d="M13 6l2 2-3 0M15 17l-2 2 0-3M5 13l1-2 2 2"/></svg>
      <svg viewBox="0 0 24 24" fill="none" stroke="#fff" stroke-width="1.4"><path d="M6 20v-6l3-3 2 2V5a1.5 1.5 0 0 1 3 0v7h3a2 2 0 0 1 2 2v6"/><rect x="14" y="2" width="5" height="6" rx="1"/></svg>
      <svg viewBox="0 0 24 24" fill="none" stroke="#fff" stroke-width="1.4"><circle cx="12" cy="8" r="4"/><circle cx="8" cy="13" r="4"/><circle cx="16" cy="13" r="4"/><text x="12" y="23.5" font-size="4" fill="#fff" stroke="none" text-anchor="middle" font-family="Quicksand, sans-serif">VEGAN</text></svg>
    </div>
    <div class="strip">
      <span class="shade">COLOR NAME</span>
      <span class="volume">15ml e 0.5oz</span>
      <span class="maker">Nordlys Studio A/S – Havnevej 12, 2450 Copenhagen, Denmark</span>
    </div>
  </section>

</body>
</html>
```